Weightloss company needs Business Card

We want a business card that is clean and professional, yet portrays that we are a friendly, innovative, and versatile program designed to fit the needs of our clients.
I would like there to be 2 sides, one side having an appointment card, and the other side containing the logo and business information. There can be decorations on both sides. The logo is attached.

Target Market(s)

Men and women 40-60

Industry/Entity Type

Business

Contact Information for Business Card

Font styles to use
Sans Serif

Requirements
Must have
• The logo, space for business information
Nice to have
• The colors in the logo
Should not have
• No pictures of people or food

```html
<!DOCTYPE html>
<html lang="en">
<head>
<meta charset="utf-8">
<title>Risewell Weightloss Business Card</title>
<link rel="stylesheet" href="https://fonts.googleapis.com/css2?family=Montserrat:wght@500;800&family=Open+Sans:wght@400;600&display=swap">
<style>
  :root {
    --red: #d9213f;
    --teal: #6fcbe0;
    --ink: #2b2b2b;
    --line: #9a9a9a;
    --paper: #ffffff;
    --paper-shade: #ececec;
    --backdrop: #e4e1dc;
  }
  * { box-sizing: border-box; margin: 0; padding: 0; }
  html, body { width: 1200px; height: 780px; overflow: hidden; }
  body {
    background: var(--backdrop);
    font-family: "Open Sans", sans-serif;
    color: var(--ink);
    position: relative;
  }
  .card {
    position: absolute;
    top: 235px;
    width: 540px;
    height: 310px;
    background: linear-gradient(160deg, var(--paper) 0%, var(--paper-shade) 100%);
    box-shadow: 0 6px 18px rgba(0,0,0,.18);
    overflow: hidden;
  }
  .card--front { left: 40px; }
  .card--back { left: 620px; }

  .front__band { position: absolute; inset: 0; }

  .brand {
    position: absolute;
    display: flex;
    align-items: center;
    gap: 10px;
    font-family: "Montserrat", sans-serif;
    font-weight: 800;
    color: var(--red);
    white-space: nowrap;
    font-size: 28px;
  }
  .brand__dot {
    width: 14px; height: 14px;
    border-radius: 50%;
    background: var(--teal);
    flex: none;
  }
  .card--front .brand { left: 76px; top: 86px; }
  .card--back .brand { left: 60px; top: 28px; }

  .contact { position: absolute; left: 34px; top: 168px; }
  .contact__name {
    font-family: "Montserrat", sans-serif;
    font-weight: 800;
    font-size: 17px;
    color: var(--red);
    letter-spacing: .3px;
  }
  .contact__title { font-size: 13px; margin-bottom: 8px; }
  .contact__line { font-size: 13px; line-height: 1.35; display: flex; align-items: center; gap: 6px; }
  .contact__icon {
    width: 15px; height: 15px;
    background: var(--red);
    border-radius: 2px;
    display: inline-flex; align-items: center; justify-content: center;
  }
  .website {
    position: absolute;
    right: 72px; bottom: 22px;
    font-size: 13px;
    color: var(--red);
  }

  .appointment { position: absolute; left: 34px; right: 34px; top: 92px; }
  .appointment__heading {
    font-size: 20px;
    color: var(--red);
    border-bottom: 1px solid var(--line);
    padding-bottom: 26px;
  }
  .days { display: flex; justify-content: space-between; margin-top: 14px; }
  .day { display: flex; align-items: center; gap: 6px; font-size: 12px; color: var(--red); }
  .day__box { width: 18px; height: 18px; border: 1px solid var(--line); background: var(--paper); }
  .field { display: flex; align-items: flex-end; gap: 10px; margin-top: 16px; font-size: 14px; color: var(--red); }
  .field__rule { flex: 1; border-bottom: 1px solid var(--line); height: 16px; }
  .field__meridiem { font-size: 12px; line-height: 1.1; }
</style>
</head>
<body>

<section class="card card--front" aria-label="Business card front">
  <svg class="front__band" width="540" height="310" viewBox="0 0 540 310" aria-hidden="true">
    <path d="M498 0 H540 V310 H498 V215 A70 70 0 0 0 498 75 Z" fill="var(--red)"/>
  </svg>
  <div class="brand"><span class="brand__dot"></span>Risewell Weightloss</div>

  <div class="contact">
    <p class="contact__name">EMPLOYEE NAME</p>
    <p class="contact__title">Your Title</p>
    <p class="contact__line">PO BOX your address,</p>
    <p class="contact__line">2nd street,USA</p>
    <p class="contact__line">
      <span class="contact__icon"><svg width="9" height="9" viewBox="0 0 10 10"><path d="M2 1 L4 1 L4.6 3.2 L3.5 4 Q4.5 6 6 6.5 L6.8 5.4 L9 6 L9 8 Q5 9 1 3.5 Z" fill="#fff"/></svg></span>123.456.0000
    </p>
    <p class="contact__line">
      <span class="contact__icon"><svg width="10" height="8" viewBox="0 0 10 8"><rect x=".5" y=".5" width="9" height="7" fill="none" stroke="#fff"/><path d="M.5 .5 L5 4.5 L9.5 .5" fill="none" stroke="#fff"/></svg></span>info@risewellmail.com
    </p>
  </div>
  <p class="website">www.risewellprogram.com</p>
</section>

<section class="card card--back" aria-label="Appointment card">
  <div class="brand"><span class="brand__dot"></span>Risewell Weightloss</div>
  <div class="appointment">
    <p class="appointment__heading">Has An Appointment On</p>
    <div class="days">
      <span class="day"><span class="day__box"></span>Mon</span>
      <span class="day"><span class="day__box"></span>Tues</span>
      <span class="day"><span class="day__box"></span>Wed</span>
      <span class="day"><span class="day__box"></span>Thur</span>
      <span class="day"><span class="day__box"></span>Fri</span>
      <span class="day"><span class="day__box"></span>Sat</span>
    </div>
    <div class="field">Date :<span class="field__rule"></span></div>
    <div class="field">Time :<span class="field__rule"></span><span class="field__meridiem">am.<br>pm.</span></div>
  </div>
</section>

</body>
</html>
```